Create a pitch deck for a specialist physical product development search firm

Please review the attached project brief and the following instructions.
I need a designer to create a 10-slide pitch deck for Velmo, a specialist recruitment partner for physical product design & development companies. The deck will be used to pitch our retained/exclusive recruitment service to potential clients.
The design should:
Follow our bold, clean brand guidelines (provided)
Feel premium, minimalist, and professional
The deck includes:
Problem statement
Our story & differentiators
Process overview
2 client case studies
Social proof/testimonials
Clear call-to-action
Deliverables:
Editable Canva file (preferred) or PowerPoint
Exported PDF
Optional: LinkedIn carousel adaptation

```html
<!DOCTYPE html>
<html lang="en">
<head>
<meta charset="utf-8">
<title>Velmo – Specialist Search Pitch Deck</title>
<link rel="stylesheet" href="https://fonts.googleapis.com/css2?family=Outfit:wght@300;400;500;600;700&display=swap">
<style>
:root{
  --stage:#2e2e2e;
  --cream:#fef0d9;
  --pale:#fbe5bd;
  --orange:#de8a08;
  --amber:#f5b83f;
  --ink:#1c1c1c;
  --muted:#4a4036;
  --white:#ffffff;
}
*{box-sizing:border-box;margin:0;padding:0}
html,body{width:1200px;height:4769px;overflow:hidden}
body{background:var(--stage);font-family:"Outfit",Arial,sans-serif;color:var(--ink);position:relative}
.slide{position:absolute;left:120px;width:960px;height:540px;background:var(--cream);overflow:hidden}
.abs{position:absolute}
.eyebrow{position:absolute;left:46px;top:34px;font-size:19px;font-weight:500;letter-spacing:5px}
.eyebrow::after{content:"";position:absolute;left:0;top:32px;width:42px;height:3px;background:var(--orange)}
.brand{position:absolute;right:18px;top:20px;display:flex;align-items:center;gap:6px;font-weight:600;font-size:19px;z-index:3}
.brand i{display:block;width:14px;height:14px;background:var(--orange);border-radius:50%}
.footer-url{position:absolute;left:0;right:0;bottom:9px;text-align:center;font-size:9px;color:var(--muted);z-index:3}
.page-no{position:absolute;right:18px;bottom:9px;font-size:11px;z-index:3}
.h2{font-size:33px;font-weight:500;line-height:1.22}
.panel-pale{background:var(--pale)}
.panel-orange{background:var(--orange)}
ul.list{list-style:none}
/* cover */
.cover-brand{position:absolute;left:0;right:0;top:150px;display:flex;justify-content:center;align-items:center;gap:30px}
.cover-brand i{display:block;width:120px;height:120px;background:var(--orange);border-radius:50%}
.cover-brand span{font-size:130px;font-weight:600;letter-spacing:-2px;line-height:1}
.cover-title{position:absolute;left:0;right:0;top:364px;text-align:center;font-size:54px;font-weight:400;letter-spacing:7px}
.cover-sub{position:absolute;left:0;right:0;top:430px;text-align:center;font-size:27px;font-weight:300}
/* problem */
.problem-cards{position:absolute;left:37px;top:267px;display:flex;gap:13px}
.problem-card{width:167px;height:207px;background:var(--white);border:1px solid #ecdcc0;padding:20px 18px}
.problem-card .icon{width:72px;height:72px;background:var(--orange);border-radius:10px;opacity:.85}
.problem-card p{margin-top:50px;font-size:12px;line-height:1.25}
/* tick rows */
.tick-row{position:absolute;display:flex;align-items:center;gap:18px;font-size:19px;line-height:1.2}
.tick-row svg{flex:none}
/* columns */
.help-col{position:absolute;top:233px;width:248px;height:225px;background:#fde3b3}
.help-col h3{height:45px;background:var(--orange);color:var(--white);font-weight:400;font-size:19px;text-align:center;line-height:45px}
.help-col ul{padding:24px 18px 0 26px}
.help-col li{font-size:15px;line-height:1.25;margin-bottom:17px;padding-left:18px;position:relative}
.help-col li::before{content:"";position:absolute;left:0;top:7px;width:4px;height:4px;border-radius:50%;background:var(--ink)}
/* delivery */
.step{position:absolute;left:74px;display:flex;align-items:center;gap:18px;font-size:13px;line-height:1.3;color:var(--muted)}
.step b{color:var(--ink);font-weight:600}
.stat{position:absolute;left:565px;display:flex;align-items:center;gap:10px;font-size:20px;font-weight:300}
.quote-card{position:absolute;left:561px;width:316px;background:var(--cream);border-radius:0 0 18px 0;padding:12px 24px;font-size:10px;line-height:1.35;color:var(--muted)}
.quote-card strong{display:block;margin-top:10px;color:var(--ink);font-weight:600;font-size:9.5px}
/* case studies */
.case-name{position:absolute;left:0;right:0;text-align:center;font-weight:600}
.case-box{position:absolute;width:278px;padding:0 26px}
.case-box h3{text-align:center;font-size:27px;font-weight:400;margin-top:24px}
.case-box ul{margin-top:26px}
.case-box li{font-size:12.5px;line-height:1.25;color:var(--muted);margin-bottom:14px;padding-left:14px;position:relative}
.case-box li::before{content:"";position:absolute;left:0;top:6px;width:3px;height:3px;border-radius:50%;background:var(--muted)}
.case-box li b{color:var(--ink);font-weight:600}
.case-box.outcome{background:var(--amber)}
.case-box.outcome li{color:#4b3514}
.case-box.pale{background:#fbe3b6}
</style>
</head>
<body>
<svg width="0" height="0" style="position:absolute">
  <defs>
    <symbol id="tick-soft" viewBox="0 0 40 40">
      <circle cx="20" cy="20" r="17" fill="#f8c978"/>
      <path d="M11 20l7 7 14-15" fill="none" stroke="#fef0d9" stroke-width="4" stroke-linecap="round" stroke-linejoin="round"/>
    </symbol>
    <symbol id="tick-badge" viewBox="0 0 44 44">
      <circle cx="22" cy="22" r="21" fill="#de8a08"/>
      <circle cx="22" cy="22" r="14" fill="#1c1c1c"/>
      <path d="M15 22l6 6 12-13" fill="none" stroke="#f5b83f" stroke-width="4" stroke-linecap="round" stroke-linejoin="round"/>
    </symbol>
  </defs>
</svg>

<!-- 1 Cover -->
<section class="slide" style="top:90px">
  <div class="cover-brand"><i></i><span>velmo</span></div>
  <h1 class="cover-title">SPECIALIST SEARCH</h1>
  <p class="cover-sub">For Physical Product Design &amp; Development</p>
</section>

<!-- 2 Problem -->
<section class="slide" style="top:668px">
  <div class="eyebrow">THE PROBLEM</div>
  <div class="brand"><i></i>velmo</div>
  <h2 class="abs" style="left:46px;top:180px;font-size:32px;font-weight:500">Why recruitment feels broken?</h2>
  <div class="problem-cards">
    <div class="problem-card"><div class="icon" role="img" aria-label="Icon of a disengaged person at a desk"></div><p>High-volume, transactional models lead to disengagement</p></div>
    <div class="problem-card"><div class="icon" role="img" aria-label="Icon of a broken handshake"></div><p>Lack of true partnership between clients &amp; recruiters</p></div>
    <div class="problem-card"><div class="icon" role="img" aria-label="Icon of a CV under a magnifying glass"></div><p>Time wasted screening irrelevant CVs</p></div>
    <div class="problem-card"><div class="icon" role="img" aria-label="Icon of a group of candidates"></div><p>Poor candidate journeys = poor hiring outcomes</p></div>
    <div class="problem-card"><div class="icon" role="img" aria-label="Icon of a pie chart"></div><p>Recruiters who don't "get" the market or what good looks like</p></div>
  </div>
  <div class="footer-url">www.teamvelmo.com</div><div class="page-no">2</div>
</section>

<!-- 3 Story -->
<section class="slide" style="top:1246px">
  <div class="abs panel-pale" style="left:0;top:0;width:480px;height:270px"></div>
  <div class="abs panel-orange" style="left:0;top:270px;width:480px;height:270px"></div>
  <div class="eyebrow">THE VELMO STORY</div>
  <div class="brand"><i></i>velmo</div>
  <h2 class="abs h2" style="left:85px;top:134px">Velmo means chord.<br>It's about harmony.</h2>
  <div class="abs" style="left:62px;top:330px;width:370px;color:var(--white);font-size:9px;line-height:1.8">
    <p>Velmo comes from an old word meaning chord—a symbol of harmony where individual notes create something greater.</p>
    <p style="margin-top:12px">I founded Velmo to bring this principle into recruitment. Too often, traditional recruitment feels transactional: high volume, low engagement, and little understanding of what makes a team resonate.</p>
    <p style="margin-top:12px">At Velmo, we help hardware brands, consultancies, and medtech innovators build teams that thrive.</p>
  </div>
  <p class="abs" style="left:581px;top:128px;font-size:19px;font-weight:500">Velmo is about:</p>
  <div class="tick-row" style="left:578px;top:194px"><svg width="38" height="38"><use href="#tick-soft"/></svg><span>Relationships over<br>transactions</span></div>
  <div class="tick-row" style="left:578px;top:270px"><svg width="38" height="38"><use href="#tick-soft"/></svg><span>Speaking your language,<br>knowing your market</span></div>
  <div class="tick-row" style="left:578px;top:360px"><svg width="38" height="38"><use href="#tick-soft"/></svg><span>Creating lasting impact for<br>candidates and clients</span></div>
  <div class="footer-url">www.teamvelmo.com</div><div class="page-no">3</div>
</section>

<!-- 4 Difference -->
<section class="slide" style="top:1824px">
  <div class="abs panel-pale" style="left:0;top:0;width:480px;height:540px"></div>
  <div class="eyebrow">THE VELMO DIFFERENCE</div>
  <div class="brand"><i></i>velmo</div>
  <h2 class="abs h2" style="left:93px;top:210px;font-size:36px">What makes<br>Velmo different?</h2>
  <div class="abs panel-orange" style="left:46px;top:422px;width:486px;height:52px;border-radius:0 0 22px 0;color:var(--white);font-size:12px;line-height:1.3;padding:10px 16px">
    "We spent a lot less time reviewing CVs as every candidate was spot on."<br><b>— Owen Harlow, Head of Engineering, Trekwell</b>
  </div>
  <div class="tick-row" style="left:564px;top:108px"><svg width="46" height="46"><use href="#tick-badge"/></svg><span>Specialist in physical product<br>development roles</span></div>
  <div class="tick-row" style="left:564px;top:207px"><svg width="46" height="46"><use href="#tick-badge"/></svg><span>Founder-led,<br>relationship-first search</span></div>
  <div class="tick-row" style="left:564px;top:295px"><svg width="46" height="46"><use href="#tick-badge"/></svg><span>Boutique, agile, and<br>quality-focused</span></div>
  <div class="tick-row" style="left:564px;top:384px"><svg width="46" height="46"><use href="#tick-badge"/></svg><span>Proven results: faster hiring<br>and better retention</span></div>
  <div class="footer-url">www.teamvelmo.com</div><div class="page-no">4</div>
</section>

<!-- 5 Who we help -->
<section class="slide" style="top:2402px">
  <div class="eyebrow">WHO WE HELP</div>
  <div class="brand"><i></i>velmo</div>
  <h2 class="abs" style="left:81px;top:150px;font-size:32px;font-weight:500">Who we help &amp; what success looks like</h2>
  <div class="help-col" style="left:81px"><h3>Typical Clients:</h3>
    <ul><li>Hardware start-ups<br>&amp; scale-ups</li><li>Design consultancies</li><li>Medtech &amp; consumer<br>health brands</li></ul></div>
  <div class="help-col" style="left:355px"><h3>Challenges:</h3>
    <ul><li>Long hiring cycles</li><li>Low candidate<br>Engagement</li><li>Difficulty finding<br>niche talent</li></ul></div>
  <div class="help-col" style="left:629px"><h3>What success looks like:</h3>
    <ul><li>Hiring within 3–6 weeks</li><li>Candidates aligned<br>&amp; excited</li><li>Predictable process<br>&amp; higher retention</li></ul></div>
  <div class="footer-url">www.teamvelmo.com</div><div class="page-no">5</div>
</section>

<!-- 6 How we deliver -->
<section class="slide" style="top:2980px">
  <div class="abs panel-pale" style="left:480px;top:0;width:480px;height:270px"></div>
  <div class="abs panel-orange" style="left:480px;top:270px;width:480px;height:270px"></div>
  <div class="eyebrow">HOW WE DELIVER</div>
  <div class="brand"><i></i>velmo</div>
  <h2 class="abs h2" style="left:74px;top:152px;font-size:35px">A partnership-led<br>process that works</h2>
  <div class="step" style="top:272px"><svg width="40" height="40" viewBox="0 0 40 40"><circle cx="20" cy="20" r="16" fill="none" stroke="#f5b83f" stroke-width="3"/><circle cx="20" cy="20" r="9" fill="none" stroke="#f5b83f" stroke-width="3"/><circle cx="20" cy="20" r="3" fill="#de8a08"/></svg><span><b>Define:</b> Understand your business,<br>team culture &amp; goals</span></div>
  <div class="step" style="top:338px"><svg width="40" height="40" viewBox="0 0 40 40"><path d="M8 14h16l-5-5M32 26H16l5 5" fill="none" stroke="#de8a08" stroke-width="3" stroke-linecap="round" stroke-linejoin="round"/></svg><span><b>Engage:</b> Exclusive, tailored<br>candidate journeys</span></div>
  <div class="step" style="top:403px"><svg width="40" height="40" viewBox="0 0 40 40"><path d="M10 21l7 7 13-15" fill="none" stroke="#f5b83f" stroke-width="4" stroke-linecap="round" stroke-linejoin="round"/></svg><span><b>Deliver:</b> Predictable outcomes<br>with high engagement</span></div>
  <div class="stat" style="top:74px"><svg width="24" height="24"><use href="#tick-soft"/></svg>100% fill rate</div>
  <div class="stat" style="top:120px"><svg width="24" height="24"><use href="#tick-soft"/></svg>97% retention after 12 months</div>
  <div class="stat" style="top:168px"><svg width="24" height="24"><use href="#tick-soft"/></svg>+92 NPS (world-class)</div>
  <div class="abs" style="left:688px;top:284px;font-size:72px;font-weight:700;color:#fbe5bd;line-height:1">“</div>
  <div class="quote-card" style="top:350px">"No agency shenanigans – helped us build<br>a professional hiring experience."<strong>— Liam Pryce, Co-Founder, Gauge Works</strong></div>
  <div class="quote-card" style="top:435px">"Compared to other recruiters, this was faster,<br>more personalised, and highly organised."<strong>— Nina Castell, CEO, Brightpath Health</strong></div>
  <div class="footer-url">www.teamvelmo.com</div><div class="page-no">6</div>
</section>

<!-- 7 Case study: Brightpath Health -->
<section class="slide" style="top:3558px">
  <div class="eyebrow">CASE STUDY: BRIGHTPATH HEALTH</div>
  <div class="brand"><i></i>velmo</div>
  <div class="case-name" style="top:132px;font-size:44px;color:#1f2a6b">brightpath</div>
  <div class="case-box pale" style="left:48px;top:222px;height:250px"><h3>Challenge:</h3>
    <ul><li>Critical leadership hire during a period of disruption</li><li>Lack of trust in recruiters due to previous poor experiences</li><li>Limited hiring budget and an unsettled team</li></ul></div>
  <div class="case-box pale" style="left:341px;top:222px;height:250px"><h3>Solution:</h3>
    <ul><li>Founder-led, transparent process to build trust</li><li><b>4 candidates shortlisted in 2 weeks</b></li><li><b>Offer accepted within 4.5 weeks</b></li></ul></div>
  <div class="case-box outcome" style="left:631px;top:222px;height:250px"><h3>Outcome:</h3>
    <ul><li>Secured a <b>CPO</b> who launched Brightpath's customer-ready product and stabilized the leadership team</li></ul></div>
  <div class="footer-url">www.teamvelmo.com</div><div class="page-no">7</div>
</section>

<!-- 8 Case study: Trekwell -->
<section class="slide" style="top:4136px">
  <div class="eyebrow">CASE STUDY: TREKWELL</div>
  <div class="brand"><i></i>velmo</div>
  <div class="abs" style="left:330px;top:119px;width:298px;height:61px;background:#2a3a3f;color:var(--white);font-size:30px;font-weight:500;display:flex;align-items:center;justify-content:center">Trekwell</div>
  <div class="case-box pale" style="left:48px;top:206px;height:291px"><h3>Challenge:</h3>
    <ul><li>9+ months of unsuccessful hiring attempts</li><li>Multiple candidate dropouts due to poor process design</li><li>Recruiters failed to deliver suitable technical talent</li><li>Limited employer brand awareness and recruitment resources</li></ul></div>
  <div class="case-box pale" style="left:341px;top:206px;height:291px"><h3>Solution:</h3>
    <ul><li>Transparent process aligned with stakeholder availability</li><li>Leveraged Trekwell's pitch deck to boost engagement</li><li><b>4 candidates shortlisted</b></li><li><b>Offer accepted within 3 weeks of engagement</b></li></ul></div>
  <div class="case-box outcome" style="left:631px;top:206px;height:291px"><h3>Outcome:</h3>
    <ul><li>Placed a <b>Principal Mechanical Engineer</b> who strengthened Trekwell's growing R&amp;D team</li></ul></div>
  <div class="footer-url">www.teamvelmo.com</div><div class="page-no">8</div>
</section>
</body>
</html>
```